Web Design Project

I need a fresh and professional look for the homepage at www.brightwavelink.com, the slider part at the top.
We do international calling calling from/to all countries in the world. For the moment, we do direct sales in Thailand, where we
are opening small kiosks on the beach fronts around thailand.
A nice looking landing page is what we are looking for.
It can be one image with room for the text to be added.
Updates
Target Market(s)
Holiday travellers. Our service allow people to call from/to any country, only paying local charges, witch represent about 95% savings compared to calling via local gsm operators. We support even the oldest GSM phones, and all countries, even those who not allow VOIP, like China.
Industry/Entity Type
Sales
Look and feel
Each slider illustrates characteristics of the customer's brand and the style your logo design should communicate.

```html
<!DOCTYPE html>
<html lang="en">
<head>
<meta charset="utf-8">
<title>BrightWaveLink — International Calling</title>
<link rel="stylesheet" href="https://fonts.googleapis.com/css2?family=PT+Sans:wght@400;700&family=PT+Sans+Narrow:wght@400;700&display=swap">
<style>
:root{
  --accent:#ee6a35;
  --header-bg:#e6e6e8;
  --ink:#111;
  --text:#333;
  --link:#1a6fd8;
  --nav:#1d1d1d;
  --line:#d9d9d9;
}
*{margin:0;padding:0;box-sizing:border-box}
html,body{width:1200px;height:1103px;overflow:hidden;background:#fff}
body{position:relative;font-family:"PT Sans",Arial,sans-serif;color:var(--text)}
.abs{position:absolute}
.top-line{left:0;top:0;width:1200px;height:3px;background:var(--accent)}
.header{left:0;top:3px;width:1200px;height:131px;background:var(--header-bg)}
.brand{left:171px;top:98px;font-size:19px;color:var(--ink);letter-spacing:.2px}
.brand-dot{left:224px;top:22px;width:34px;height:34px;border-radius:50%;background:var(--accent)}
.account{left:935px;top:11px;font-size:12px;color:var(--ink);display:flex}
.account span{padding:0 8px;line-height:26px}
.account span+span{border-left:1px solid #c8c8c8}
.search{left:827px;top:42px;width:199px;height:28px;background:#fff;border-radius:6px;font-size:12px;color:var(--ink);padding:6px 12px}
.search svg{position:absolute;right:7px;top:5px}
.nav{left:366px;top:90px;width:661px;height:35px;background:linear-gradient(#3a3a3a,var(--nav) 50%,#0d0d0d);border-radius:6px;display:flex;align-items:center}
.nav a{color:#fff;font-size:11.5px;text-decoration:none;height:100%;display:flex;align-items:center;justify-content:center;border-right:1px solid #444}
.nav a:last-child{border-right:0}
.slider{left:3px;top:138px;width:1195px;height:419px;border:1px solid var(--line);background:linear-gradient(#fff 0,#fff 74%,#e2e2e4 100%)}
.headline{left:271px;top:226px;font-family:"PT Sans Narrow",sans-serif;font-size:26px;line-height:37px;color:var(--ink)}
.headline .lead{color:var(--accent)}
.btn-more{left:274px;top:347px;width:87px;height:31px;background:#000;color:var(--accent);font-family:"PT Sans Narrow",sans-serif;font-size:19px;text-align:center;line-height:31px}
.arrow{top:320px}
.people{left:641px;top:148px;width:310px;height:383px;border-radius:40px 40px 10px 10px;background:linear-gradient(90deg,#55a84f,#e8436a 30%,#d8a9c8 55%,#3fa7a0 70%,#7a5aa8 90%)}
.intro{left:175px;top:585px;width:700px;font-family:"PT Sans Narrow",sans-serif;font-size:16.5px;line-height:27.7px;color:var(--ink)}
.globe{left:891px;top:584px;width:138px;height:134px;border-radius:50%;background:radial-gradient(circle,#2c6de0 40%,#9db9f0 75%,#fff 76%)}
.divider{left:175px;top:736px;width:855px;height:30px;background:linear-gradient(#fff,#ececec);border-bottom:2px solid #d6d6d6;border-radius:0 0 50% 50%/0 0 14px 14px}
.card{top:785px;width:272px;height:179px;border:1px solid var(--line);border-radius:4px;background:linear-gradient(#fff 60%,#f1f1f1);box-shadow:0 2px 3px rgba(0,0,0,.05)}
.card h2{position:absolute;left:19px;top:12px;font-family:"PT Sans Narrow",sans-serif;font-weight:400;font-size:21px;color:var(--link)}
.card .photo{position:absolute;left:1px;bottom:1px;width:118px;height:128px}
.card .blurb{position:absolute;left:127px;top:51px;width:128px;font-size:11.5px;line-height:18.5px;text-align:justify;color:#444}
.card .more{position:absolute;left:127px;top:148px;font-size:11.5px;color:var(--link)}
.news-item{position:absolute;left:19px;width:240px;font-size:11.5px;line-height:14px;color:#444;padding-left:23px}
.news-item svg{position:absolute;left:0;top:1px}
.news-item .more{position:static;display:block;margin-top:7px;color:var(--link)}
.footer-band{left:0;top:984px;width:1200px;height:20px;background:linear-gradient(#e4e4e4,#fff)}
.footer-links{left:0;top:1028px;width:1200px;text-align:center;font-size:12px;color:var(--link)}
.footer-links span{color:#888;padding:0 4px}
.copyright{left:0;top:1051px;width:1200px;text-align:center;font-size:12px;color:var(--link)}
</style>
</head>
<body>
<div class="abs top-line"></div>
<header class="abs header"></header>
<div class="abs brand-dot"></div>
<div class="abs brand">brightwavelink.com</div>
<div class="abs account"><span>Register</span><span>Login</span></div>
<div class="abs search">Search
  <svg width="18" height="18" viewBox="0 0 18 18"><circle cx="7" cy="7" r="5" fill="#e8f1fb" stroke="#7a9cc4" stroke-width="1.5"/><line x1="11" y1="11" x2="16" y2="16" stroke="#555" stroke-width="2.5" stroke-linecap="round"/></svg>
</div>
<nav class="abs nav">
  <a style="width:73px">HOME</a><a style="width:100px">MOBILEHOME</a><a style="width:62px">SHOP</a><a style="width:79px">ABOUT US</a><a style="width:92px">OUR SERVICES</a><a style="width:123px">NEWS &amp; PROMOTIONS</a><a style="width:132px">GETTING STARTED</a>
</nav>

<section class="abs slider"></section>
<div class="abs headline"><div class="lead">We Support everything,</div><div>from the oldest GSM mobile phone,</div><div>to the newest smartphone available</div></div>
<div class="abs btn-more">Read More</div>
<svg class="abs arrow" style="left:180px" width="34" height="20" viewBox="0 0 34 20"><path d="M33 10H2M11 2 2 10l9 8" fill="none" stroke="#333" stroke-width="2"/></svg>
<svg class="abs arrow" style="left:989px" width="34" height="20" viewBox="0 0 34 20"><path d="M1 10h31M23 2l9 8-9 8" fill="none" stroke="#333" stroke-width="2"/></svg>
<div class="abs people" role="img" aria-label="Group of five young travellers in colourful tops talking on mobile phones"></div>

<p class="abs intro">Lorem Ipsum is simply dummy text of the printing and typesetting industry. Lorem Ipsum has been the industry's standard dummy text ever since the 1500s, when an unknown printer took a galley of type and scrambled it to make a type specimen book. It has survived not only five centuries, but also the leap into electronic typesetting, remaining essentially unchanged. It was popularised in the 1960s with the release of Lettrafold sheets containing Lorem Ipsum passages, and more recently with desktop publishing software like Pagewright Studio including versions of Lorem Ipsum.</p>
<div class="abs globe" role="img" aria-label="Blue globe surrounded by a ring of numbered dial buttons with a red pointer"></div>
<div class="abs divider"></div>

<article class="abs card" style="left:178px">
  <h2>Our Services</h2>
  <div class="photo" role="img" aria-label="Smiling blonde woman on the phone" style="background:linear-gradient(135deg,#f3e2b8,#d9b87a 60%,#c99a6a)"></div>
  <p class="blurb">Lorem Ipsum is simply dummy text of the printing and typesetting industry. Lorem Ipsum has been the industry's</p>
  <span class="more">Read More &gt;&gt;</span>
</article>
<article class="abs card" style="left:469px">
  <h2>Shop</h2>
  <div class="photo" role="img" aria-label="Smartphone in front of a blue globe" style="background:radial-gradient(circle at 40% 55%,#6b8fc0,#b8cde6 45%,#fff 70%)"></div>
  <p class="blurb">Lorem Ipsum is simply dummy text of the printing and typesetting industry. Lorem Ipsum has been the industry's</p>
  <span class="more">Read More &gt;&gt;</span>
</article>
<article class="abs card" style="left:756px">
  <h2>News</h2>
  <div class="news-item" style="top:59px">
    <svg width="16" height="14" viewBox="0 0 16 14"><rect x=".5" y=".5" width="15" height="13" fill="#fff" stroke="#8aa"/><path d="M3 4h10M3 7h10M3 10h10" stroke="#6b8fb5"/></svg>
    Lorem Ipsum is simply dummy text of the printing and typesetting industry.<span class="more">Read More &gt;&gt;</span>
  </div>
  <div class="news-item" style="top:118px">
    <svg width="16" height="14" viewBox="0 0 16 14"><rect x=".5" y=".5" width="15" height="13" fill="#fff" stroke="#8aa"/><path d="M3 4h10M3 7h10M3 10h10" stroke="#6b8fb5"/></svg>
    Lorem Ipsum is simply dummy text of the printing and typesetting industry.<span class="more">Read More &gt;&gt;</span>
  </div>
</article>

<div class="abs footer-band"></div>
<footer>
  <div class="abs footer-links">Getting Started <span>|</span> Home <span>|</span> MobileHOME <span>|</span> Shop <span>|</span> About Us <span>|</span> Our Services <span>|</span> News &amp; Promotions <span>|</span> Terms Of Use <span>|</span> Privacy Statement</div>
  <div class="abs copyright">Copyright 2012 by Brightwave Telecom Ltd.</div>
</footer>
</body>
</html>
```